law firm business cards

I need a business card using my existing logo. Two sided is best because there is a lot of information that needs to go on the card. Use the same general color scheme as logo, but I need one set with the blue background of my website (www.kestonlegalgroup.com), and one set with white background (to see which one I like best).

Information that must be on there:
Darren P. Holloway
Board Certified Civil Trial Specialist
738 Brindlewood Ave., Suite 2300
Raleigh, NC 27699

T 919-555-0142
F 919-555-0187

www.kestonlegalgroup.com
darren@kestonlegalgroup.com

Personal Injury | Criminal Law (to separate the two, pls use a bullet point or pipeline symbol "|"

If there is a way to work in the QRVC logo (maybe at the bottom somewhere), put it in, but don't let it detract from the main logo too much.

Also, if there is a way to work it in, put in somewhere: Former Insurance Company Attorney | Former Criminal Prosecutor (to separate the two, pls use a bullet point or pipeline symbol "|"

```html
<!DOCTYPE html>
<html lang="en">
<head>
<meta charset="utf-8">
<title>Keston Legal — Business Cards</title>
<link rel="stylesheet" href="https://fonts.googleapis.com/css2?family=Didact+Gothic&display=swap">
<style>
  :root {
    --stage: #e6e3df;
    --brand-blue: #2f80c0;
    --brand-red: #e2103f;
    --paper: #f4f4f4;
    --ink: #3a3a3a;
    --white: #ffffff;
    --seal: #d4dbe6;
    --seal-edge: #8fa2bd;
    --shadow: rgba(0, 0, 0, 0.18);
  }
  * { box-sizing: border-box; margin: 0; padding: 0; }
  html, body {
    width: 1200px; height: 900px; overflow: hidden;
    background: var(--stage);
    font-family: "Didact Gothic", "Century Gothic", sans-serif;
  }
  .stage { position: relative; width: 1200px; height: 900px; }
  .card {
    position: absolute; left: 280px;
    width: 640px; height: 366px;
    overflow: hidden;
    box-shadow: 0 6px 18px var(--shadow);
  }

  /* Front: blue */
  .card--front { top: 64px; background: var(--brand-blue); }
  .card--front .wordmark {
    position: absolute; left: 250px; top: 112px;
    display: flex; align-items: center; gap: 10px;
    color: var(--white); font-size: 34px; letter-spacing: 2px;
  }
  .wordmark__square { width: 22px; height: 22px; border: 2px solid currentColor; }
  .card--front .credential-band {
    position: absolute; left: 0; right: 0; top: 226px; height: 38px;
    background: var(--brand-red);
    color: var(--white);
    font-size: 12.5px; letter-spacing: 1.4px;
    display: flex; align-items: center; padding-left: 34px;
  }

  /* Back: white */
  .card--back { top: 470px; background: var(--paper); }
  .card--back .wordmark {
    position: absolute; left: 64px; top: 30px;
    display: flex; align-items: center; gap: 10px;
    color: var(--ink); font-size: 28px; letter-spacing: 2px;
  }
  .card--back .wordmark__square { width: 18px; height: 18px; }
  .seal {
    position: absolute; left: 28px; top: 96px;
    width: 46px; height: 46px; border-radius: 50%;
    background: var(--seal); border: 2px solid var(--seal-edge);
  }
  .swoosh { position: absolute; inset: 0; }
  .practice-areas {
    font-family: "Didact Gothic", "Century Gothic", sans-serif;
    font-size: 15px; letter-spacing: 2px;
  }
  .contact {
    position: absolute; left: 340px; top: 82px;
    color: var(--ink); font-size: 13.5px; letter-spacing: 1px; line-height: 1.45;
  }
  .contact__name {
    font-size: 13px; letter-spacing: 3px; text-transform: uppercase;
    font-weight: bold;
  }
  .contact__title { color: var(--brand-red); margin-bottom: 6px; }
  .contact__row { display: flex; align-items: center; gap: 8px; }
  .contact__icon { width: 13px; height: 13px; flex: none; }
</style>
</head>
<body>
<main class="stage">

  <section class="card card--front" aria-label="Business card front">
    <div class="wordmark"><span class="wordmark__square"></span><span>KESTON LEGAL</span></div>
    <div class="credential-band">Former Insurance Company Attorney, Former Criminal Prosecutor</div>
  </section>

  <section class="card card--back" aria-label="Business card back">
    <svg class="swoosh" viewBox="0 0 640 366" width="640" height="366">
      <path d="M0 150 C 150 230, 400 300, 640 332 L 640 366 L 0 366 Z" fill="var(--brand-blue)"/>
      <path d="M0 156 C 150 238, 400 306, 640 338 L 640 366 L 0 366 Z" fill="var(--brand-red)"/>
      <text class="practice-areas" x="110" y="262" transform="rotate(14 110 262)" fill="var(--white)">Personal Injury  |  Criminal Law</text>
    </svg>

    <div class="wordmark"><span class="wordmark__square"></span><span>KESTON LEGAL</span></div>
    <div class="seal" role="img" aria-label="Certification seal"></div>

    <div class="contact">
      <p class="contact__name">Darren P. Holloway</p>
      <p class="contact__title">Board Certified Civil Trial Specialist</p>
      <p>738 Brindlewood Ave., Suite 2300</p>
      <p>Raleigh, NC 27699</p>
      <p class="contact__row">
        <svg class="contact__icon" viewBox="0 0 16 16"><circle cx="8" cy="8" r="8" fill="var(--brand-blue)"/><path d="M5 4h2l1 2-1 1a5 5 0 0 0 2 2l1-1 2 1v2a1 1 0 0 1-1 1A7 7 0 0 1 4 5a1 1 0 0 1 1-1z" fill="var(--white)"/></svg>
        <span>919-555-0142</span>
      </p>
      <p class="contact__row">
        <svg class="contact__icon" viewBox="0 0 16 16"><circle cx="8" cy="8" r="8" fill="var(--brand-blue)"/><rect x="4" y="6" width="8" height="6" rx="1" fill="var(--white)"/><rect x="5.5" y="3.5" width="5" height="3" fill="var(--white)"/></svg>
        <span>919-555-0187</span>
      </p>
      <p class="contact__row">
        <svg class="contact__icon" viewBox="0 0 16 16"><circle cx="8" cy="8" r="8" fill="var(--brand-blue)"/><circle cx="8" cy="8" r="4.5" fill="none" stroke="var(--white)" stroke-width="1.2"/><path d="M3.5 8h9M8 3.5v9" stroke="var(--white)" stroke-width="1"/></svg>
        <span>www.kestonlegalgroup.com</span>
      </p>
      <p class="contact__row">
        <svg class="contact__icon" viewBox="0 0 16 16"><circle cx="8" cy="8" r="8" fill="var(--brand-blue)"/><rect x="3.5" y="5" width="9" height="6" fill="none" stroke="var(--white)" stroke-width="1.2"/><path d="M3.5 5l4.5 3.5 4.5-3.5" fill="none" stroke="var(--white)" stroke-width="1.2"/></svg>
        <span>darren@kestonlegalgroup.com</span>
      </p>
    </div>
  </section>

</main>
</body>
</html>
```